IT Company needs stationary design

Business cards, MS Word, PowerPoint, A4 notepad design base on our company logo. This must be a set of templates in the same style which could be used both for printable documents as well as for documents shared digitally via email, website etc. This should be a modern design which is still professional, so make sure content is well readable both in MS Word and MS PowerPoint templates.

Target Market(s)

SME and Corporate

Industry/Entity Type

It Company

Font styles to use
Sans Serif

Colors
0455a3
0692cd
f37122
ffc214

Requirements
Must have
• 1) Business cards design: modern but still professional
• 2) MS Word: mostly for IT project documents (business analysis, reports, specifications, etc.) must be professional and easy readable.
• 3) MS PowerPoint: first slide, normal slide, last slide.
• 4) A4 notepad: header (must), footer (must), some light design on the background (optionally)
Nice to have
• Business cards design: would be nice to have 2-4 color variations of the same design from one side - cover (for example part of the cards are blue, part of the cards are orange) and other side with contact details is identical.

```html
<!DOCTYPE html>
<html lang="en">
<head>
<meta charset="UTF-8">
<title>Corvantic Business Card</title>
<link href="https://fonts.googleapis.com/css2?family=Source+Sans+3:wght@400;600&display=swap" rel="stylesheet">
<style>
  :root {
    --page-bg: #e6e7e9;
    --panel-dark-top: #3a3b3d;
    --panel-dark-mid: #1c1d1f;
    --panel-dark-edge: #0d0d0e;
    --panel-light: #d9dadc;
    --panel-light-edge: #c9cbce;
    --brand-blue: #0692cd;
    --brand-orange: #f37122;
    --text-light: #e4e4e4;
    --logo-ink: #2a2b2d;
  }
  * { margin: 0; padding: 0; box-sizing: border-box; }
  html, body {
    width: 1200px;
    height: 969px;
    overflow: hidden;
  }
  body {
    background: var(--page-bg);
    font-family: "Source Sans 3", "Helvetica Neue", Arial, sans-serif;
    position: relative;
  }
  .business-card {
    position: absolute;
    left: 100px;
    top: 200px;
    width: 1000px;
    height: 569px;
    display: flex;
    box-shadow: 0 10px 30px rgba(0,0,0,0.18);
    border: 1px solid rgba(255,255,255,0.6);
  }
  .contact-side {
    width: 488px;
    height: 100%;
    background: linear-gradient(90deg, var(--panel-dark-top) 0%, var(--panel-dark-mid) 55%, var(--panel-dark-edge) 100%);
    padding: 94px 0 0 52px;
    color: var(--text-light);
  }
  .person-name {
    font-size: 32px;
    font-weight: 600;
    color: var(--brand-blue);
    letter-spacing: 0.5px;
    line-height: 1;
  }
  .person-title {
    font-size: 24px;
    font-weight: 400;
    color: var(--brand-orange);
    margin-top: 8px;
    line-height: 1;
  }
  .address {
    margin-top: 54px;
    font-size: 24px;
    line-height: 33px;
  }
  .contact-list {
    list-style: none;
    margin-top: 22px;
    font-size: 24px;
  }
  .contact-list li {
    display: flex;
    align-items: center;
    height: 32.5px;
  }
  .contact-icon {
    width: 22px;
    height: 22px;
    margin-right: 20px;
    fill: var(--brand-blue);
    flex-shrink: 0;
  }
  .brand-side {
    flex: 1;
    height: 100%;
    background: linear-gradient(160deg, #e4e5e7 0%, var(--panel-light) 50%, var(--panel-light-edge) 100%);
    position: relative;
  }
  .brand-lockup {
    position: absolute;
    left: -60px;
    top: 220px;
    display: flex;
    align-items: center;
  }
  .brand-dot {
    width: 122px;
    height: 122px;
    border-radius: 50%;
    background: var(--brand-blue);
    margin-right: 26px;
  }
  .brand-name {
    font-size: 66px;
    font-weight: 400;
    color: var(--logo-ink);
    letter-spacing: 1px;
    line-height: 1;
  }
</style>
</head>
<body>
  <div class="business-card">
    <section class="contact-side">
      <h1 class="person-name">MARK ELLISON</h1>
      <p class="person-title">PRESIDENT</p>
      <p class="address">2710 Harborview Lane<br>Glen Haven, NY 11020</p>
      <ul class="contact-list">
        <li>
          <svg class="contact-icon" viewBox="0 0 24 24" aria-hidden="true"><path d="M3 8c0-2 4-4 9-4s9 2 9 4v2h-5V8H8v2H3zM6 11h12l2 9H4z"/></svg>
          555 8412 3097
        </li>
        <li>
          <svg class="contact-icon" viewBox="0 0 24 24" aria-hidden="true"><path d="M7 1h10a2 2 0 0 1 2 2v18a2 2 0 0 1-2 2H7a2 2 0 0 1-2-2V3a2 2 0 0 1 2-2zm0 3v14h10V4zm5 15.5a1.2 1.2 0 1 0 0 2.4 1.2 1.2 0 0 0 0-2.4z"/></svg>
          555 3761 2048
        </li>
        <li>
          <svg class="contact-icon" viewBox="0 0 24 24" aria-hidden="true"><path d="M6 2h12v6H6zM3 9h18v9h-3v4H6v-4H3zm5 6v5h8v-5z"/></svg>
          555 4690 1735
        </li>
        <li>
          <svg class="contact-icon" viewBox="0 0 24 24" aria-hidden="true"><path d="M2 6h20v12H2zm2 2v.5l8 5 8-5V8l-8 5z"/></svg>
          mark@corvantic.com
        </li>
        <li>
          <svg class="contact-icon" viewBox="0 0 24 24" aria-hidden="true"><circle cx="12" cy="12" r="10"/><path d="M8 6c2 1 3 3 2 5s-3 2-3 4 2 3 2 5M15 4c-1 2 1 3 3 4s2 4 0 6-2 4-2 5" stroke="#1c1d1f" stroke-width="1.6" fill="none"/></svg>
          www.corvantic.com
        </li>
      </ul>
    </section>
    <section class="brand-side">
      <div class="brand-lockup">
        <span class="brand-dot"></span>
        <span class="brand-name">corvantic</span>
      </div>
    </section>
  </div>
</body>
</html>
```